Online Pet food and accessories

Hi, I have recently taken over the website www.furnestmarket.com. We sell online a variety of pet foods and accessories for dogs, cats, rabbits, birds etc.

We are looking to change the look of the website, logo and banners.

The layout is to remain the same, looking for a more modern, upmarket look to the site.

Colours and logo are open to designer interpretation at this stage, and regular feedback will be given so we can define the direction of the site.

The final design should convey class, strength and trust.
Updates

Hello Designers, thanks for your submissions to date.  Can we play around with the logo as well, as it is not something that seemed to have hit the mark when I took over the business.  I really want to lose the design from the website as is, ie the paw prints on the background of the page, and the logo.  Also we can lose the introduction on the main page of the site as I do not consider this a necessary part of the design.  Once again, thank you for your submissions so far.

Trevor
 

Looking for a new logo as well.  Some good designs, but logo is still the same.

Please leave off the company and trading name, address and contact phone number.

I also need a link to facebook and twitter.

Thanks for all your exceptional work thus far.

Regards

Trevor

Industry/Entity Type

Pet

Requirements
Must have
• One of the banner ads should indicate that we deliver to the Sydney Metropolitan Area, and now also to the NSW Central Coast.

Another Idea would be to incorporate a "Weekly Deal".

```html
<!DOCTYPE html>
<html lang="en">
<head>
<meta charset="utf-8">
<title>Furnest Market – Online Pet Food</title>
<link href="https://fonts.googleapis.com/css2?family=Arimo:wght@400;700&display=swap" rel="stylesheet">
<style>
:root{
  --page:#ffffff;
  --sky:#6f9ad6;
  --sky-light:#a9c6ec;
  --green-dark:#1b7a32;
  --green-deep:#0d5f26;
  --olive:#86ad3f;
  --olive-text:#6fa33a;
  --cream:#f2f1e6;
  --mint:#eaf3de;
  --red:#e3232a;
  --orange:#f06a1e;
  --text:#111111;
  --grey:#e5e5e5;
  --btn:#9b9b9b;
  --line:#9a9a9a;
}
*{box-sizing:border-box;margin:0;padding:0}
html,body{width:1200px;height:900px;overflow:hidden;background:var(--page);font-family:"Arimo",Arial,sans-serif;color:var(--text)}
.site{position:absolute;left:322px;top:12px;width:568px;height:888px;box-shadow:0 0 6px rgba(0,0,0,.35);background:#fff}
.abs{position:absolute}

.header{left:0;top:0;width:568px;height:86px;background:linear-gradient(180deg,var(--sky) 0%,var(--sky-light) 70%,#cfe0b8 100%)}
.header .tree{right:80px;top:0;width:150px;height:86px;background:radial-gradient(ellipse at 50% 35%,#1f3a17 0%,#2e4d20 45%,transparent 70%)}
.brand{left:12px;top:22px;display:flex;align-items:center;gap:6px;font-size:26px;font-weight:700;color:#e9e84a;letter-spacing:.5px}
.brand .dot{width:16px;height:16px;border-radius:50%;background:#e9e84a}

.nav{left:0;top:86px;width:568px;height:22px;background:var(--green-dark);display:flex;justify-content:space-around;align-items:center;font-size:8px;color:#fff}
.nav .current{color:var(--red)}
.grass{left:0;top:108px;width:568px;height:5px;background:#8fbf45}

.hero{left:0;top:113px;width:568px;height:203px;background:#fff}
.hero-title{left:0;top:77px;width:166px;text-align:center;color:var(--red);font-weight:700;font-size:15px;line-height:21px}
.hero-photo{left:156px;top:4px;width:404px;height:178px;background:radial-gradient(ellipse at 50% 55%,#b9a48a 0%,#8c7a66 35%,#e8e3dc 70%,#fff 100%);border-radius:8px}
.hero-delivery{left:0;top:186px;width:568px;text-align:right;padding-right:20px;color:var(--orange);font-size:12px}

.sidebar{left:0;top:316px;width:119px;height:549px;background:var(--green-deep)}
.cat-head{left:0;top:0;width:119px;height:20px;background:var(--green-dark);color:#fff;font-weight:700;font-size:12px;text-align:center;line-height:20px;letter-spacing:.5px}
.cat-list{left:2px;top:20px;width:117px;list-style:none}
.cat-list li{height:24.2px;margin-bottom:.8px;background:var(--mint);color:var(--olive-text);font-size:9px;font-weight:700;display:flex;align-items:center;justify-content:center;text-align:center;line-height:10px}
.cat-list li.tall{height:28px}
.newsletter{left:4px;top:355px;width:111px;height:80px;background:var(--cream);text-align:center;font-weight:700}
.newsletter h3{font-size:11.5px;margin-top:5px;letter-spacing:.4px}
.newsletter .offer{color:var(--red);font-size:8.5px;line-height:12px;margin-top:3px}
.newsletter .cta{font-size:8.5px;line-height:13px;margin-top:3px}
.signup{left:4px;top:440px;width:111px;height:14px;display:flex;gap:2px}
.signup span{flex:1;background:#fff;border:1px solid #bbb;font-size:6.5px;color:#999;padding-left:6px;line-height:12px;font-weight:400}
.signup b{background:#111;color:#fff;font-size:7px;padding:0 3px;line-height:14px}

.welcome{left:119px;top:316px;width:449px;height:38px;background:var(--olive);color:#fff;font-size:19px;font-weight:400;text-align:center;line-height:38px}
.intro{left:119px;top:358px;width:449px;text-align:center;font-size:9.5px;line-height:13.5px}
.intro strong{color:var(--red)}
.badges{left:443px;top:403px;width:118px;height:22px;display:grid;grid-template-columns:repeat(4,1fr);grid-template-rows:repeat(2,1fr);gap:2px 4px}
.badges i{display:block;background:#d93a2a;border-radius:2px}
.badges i:nth-child(odd){background:#e6a228}

.specials-bar{left:119px;top:429px;width:449px;height:27px;background:var(--green-dark)}
.pay-badge{left:7px;top:6px;width:62px;height:15px;background:#fff;border-radius:2px}
.specials-bar h2{position:absolute;left:0;width:449px;text-align:center;color:#fff;font-size:14px;line-height:27px;letter-spacing:.5px}
.account{right:12px;top:7px;background:#fff;font-size:7.5px;padding:2px 4px}

.info{left:119px;top:456px;width:449px;height:54px;background:var(--grey);font-size:7.5px;line-height:10px}
.info .pay{left:10px;top:6px}
.info .email{color:var(--orange);font-weight:700}
.info .freight{left:198px;top:8px;width:245px}
.info .freight div{display:flex}
.info .freight div span:first-child{width:60px;flex:none}

.grid{left:119px;top:510px;width:449px;height:355px}
.cell{position:absolute;border-right:1px solid var(--line);border-bottom:1px solid var(--line)}
.weekly{left:0;top:0;width:222px;height:119px;background:var(--mint);box-shadow:1px 2px 3px rgba(0,0,0,.4)}
.weekly h2{position:absolute;left:0;top:12px;width:216px;text-align:center;color:var(--red);font-size:15px}
.weekly .name{left:24px;top:48px;width:84px;text-align:center;font-size:9px;font-weight:700;line-height:15px}

.product{position:absolute;width:112px;height:118px;font-size:8px;font-weight:700}
.product .title{position:absolute;left:0;width:112px;text-align:center;font-size:7.5px}
.product .title.side{left:15px;width:auto;text-align:left}
.photo{position:absolute;border-radius:4px}
.meat{background:linear-gradient(135deg,#b24a6a,#7a2444)}
.bag-red{background:linear-gradient(160deg,#3a1a18,#b01e1e)}
.bag-orange{background:linear-gradient(160deg,#3a1a18,#e0801e)}
.bag-blue{background:linear-gradient(160deg,#1b3f8c,#2a5cb8)}
.bag-yellow{background:linear-gradient(160deg,#f5d21e,#d8a81a)}
.bag-green{background:linear-gradient(180deg,#1f7a3a 0%,#f4f4f0 30%,#e8efe2 100%)}
.bag-white{background:linear-gradient(180deg,#b31e24 0%,#f4f4f0 30%,#efe6e6 100%)}
.btns{position:absolute;font-size:8.5px;font-weight:400;display:flex;gap:4px;align-items:center}
.btns .price{font-weight:700;font-size:8px;margin-right:6px}
.btns .view{background:var(--btn);color:#fff;padding:0 3px;line-height:10px}

.footer{left:0;top:865px;width:568px;height:23px;background:var(--olive);display:flex;align-items:center;justify-content:center}
.footer span{font-size:10px;font-weight:700;color:#e9e84a}
</style>
</head>
<body>
<div class="site">
  <header>
    <div class="abs header">
      <div class="abs tree" role="img" aria-label="Tree on a hill under blue sky"></div>
      <div class="abs brand"><span>FURNEST MARKET</span><span class="dot"></span></div>
    </div>
    <nav class="abs nav">
      <span class="current">Home</span><span>Why Fresh Meat?</span><span>Dog Foods</span><span>Cat Foods</span><span>Treats</span><span>Vet Lines</span><span>Accessories</span><span>Bird Seed &amp; Small Animal Foods</span>
    </nav>
    <div class="abs grass"></div>
  </header>

  <section class="abs hero">
    <div class="abs hero-title">FRESH MEATS<br>For DOGS &amp; CATS</div>
    <div class="abs hero-photo" role="img" aria-label="Puppy, parrot, rabbit, cat and chick sitting together"></div>
    <div class="abs hero-delivery">We Deliver to Sydney Metropolitan Area and Now Also the NSW Central Coast</div>
  </section>

  <aside class="abs sidebar">
    <div class="abs cat-head">CATEGORIES</div>
    <ul class="abs cat-list">
      <li>Dog Foods</li><li>Cat Foods</li><li>Treats</li><li>Vet Lines</li>
      <li class="tall">Bird Seed &amp;<br>Small Animal Food</li>
      <li>Accessories</li><li>Tags</li><li>Pawcoat Fresh</li><li>Meat Bird Seeds</li>
      <li>Vantage Vitalis</li><li>Canine Senior Active</li><li>Doggy Puppy Regal</li><li>Canine Senior Active</li>
    </ul>
    <div class="abs newsletter">
      <h3>NEWSLETTER</h3>
      <div class="offer">New Products<br>Special Offers</div>
      <div class="cta">Sign Up for Our<br>Mailing List NOW!</div>
    </div>
    <div class="abs signup"><span>Enter Your Email</span><b>Submit</b></div>
  </aside>

  <main>
    <h1 class="abs welcome">Welcome to Furnest Market Online</h1>
    <p class="abs intro">We Specialise in <strong>FRESH MEATS</strong> for Dogs &amp; Cats.<br>We also carry a range of Premium Dry Foods, Accesories, Vet Products and Bird Seeds.<br>Our aim is to offer high qualiy products at a competitive price, shipped to your door<br>as quickly as possible.</p>
    <div class="abs badges" role="img" aria-label="Stocked brand badges"><i></i><i></i><i></i><i></i><i></i><i></i><i></i><i></i></div>

    <div class="abs specials-bar">
      <div class="abs pay-badge" role="img" aria-label="Accepted payment badge"></div>
      <h2>OUR SPECIALS</h2>
      <div class="abs account">Welcome &nbsp;Log In &nbsp;(empty)</div>
    </div>

    <div class="abs info">
      <div class="abs pay">Payment Types:<br>-Direct Deposit<br>-QuickPay, Credit Cards<br>&nbsp;No QuickPay Account Needed for Credit Cards<br><span class="email">sales@furnestmarket.com For More Info</span></div>
      <div class="abs freight">
        <div><span>Freight Charges:</span><span>Option 1 - $7.95 without Fresh Meat Orders up to 25g<br>&nbsp;&nbsp;&nbsp;&nbsp;&nbsp;&nbsp;&nbsp;&nbsp;&nbsp;Additional $4.95 for every 25kg.</span></div>
        <div style="margin-top:5px"><span></span><span>Option 2 - $10 with Fresh Meat Orders. No Weight Limit</span></div>
      </div>
    </div>

    <section class="abs grid">
      <div class="cell weekly">
        <h2>Special of the Week</h2>
        <div class="abs name">Chicken Mince<br>$12.95</div>
        <div class="photo meat" style="left:112px;top:38px;width:84px;height:72px" role="img" aria-label="Chicken mince rolls"></div>
        <div class="btns" style="left:46px;top:94px"><span class="view">view</span><span>cart</span></div>
      </div>
      <div class="cell" style="left:222px;top:0;width:227px;height:119px">
        <div class="product" style="left:0;top:0"><div class="title" style="top:13px">Beef Mince</div><div class="photo meat" style="left:22px;top:30px;width:72px;height:60px" role="img" aria-label="Beef mince rolls"></div><div class="btns" style="left:18px;top:104px"><span class="price">$43.95</span><span class="view">view</span><span>cart</span></div></div>
        <div class="product" style="left:112px;top:0"><div class="title" style="top:15px">Pork Mince</div><div class="photo meat" style="left:22px;top:30px;width:72px;height:60px" role="img" aria-label="Pork mince rolls"></div><div class="btns" style="left:18px;top:104px"><span class="price">$43.95</span><span class="view">view</span><span>cart</span></div></div>
      </div>

      <div class="cell" style="left:0;top:119px;width:222px;height:112px">
        <div class="product" style="left:0;top:0"><div class="title side" style="top:30px">Hollie</div><div class="photo bag-red" style="left:48px;top:14px;width:50px;height:72px" role="img" aria-label="Dry dog food bag"></div><div class="btns" style="left:15px;top:93px"><span class="price">$43.95</span><span class="view">view</span><span>cart</span></div></div>
        <div class="product" style="left:108px;top:0"><div class="title side" style="top:33px">Hollie</div><div class="photo bag-orange" style="left:48px;top:14px;width:50px;height:72px" role="img" aria-label="Dry dog food bag"></div><div class="btns" style="left:20px;top:93px"><span class="price">$43.95</span><span class="view">view</span><span>cart</span></div></div>
      </div>
      <div class="cell" style="left:222px;top:119px;width:227px;height:112px">
        <div class="product" style="left:0;top:0"><div class="title side" style="top:34px;left:12px">Hollie</div><div class="photo bag-blue" style="left:48px;top:16px;width:50px;height:70px" role="img" aria-label="Dry dog food bag"></div><div class="btns" style="left:12px;top:92px"><span class="price">$43.95</span><span class="view">view</span><span>cart</span></div></div>
        <div class="product" style="left:112px;top:0"><div class="title side" style="top:34px;left:12px">Hollie</div><div class="photo bag-yellow" style="left:45px;top:14px;width:42px;height:72px" role="img" aria-label="Working dog food bag"></div><div class="btns" style="left:18px;top:92px"><span class="price">$43.95</span><span class="view">view</span><span>cart</span></div></div>
      </div>

      <div class="cell" style="left:0;top:231px;width:222px;height:124px;border-bottom:none">
        <div class="product" style="left:0;top:0"><div class="title side" style="top:34px">Hollie<br>Lite</div><div class="photo bag-green" style="left:55px;top:12px;width:48px;height:80px" role="img" aria-label="Lite dog food bag"></div><div class="btns" style="left:19px;top:103px"><span class="price">$43.95</span><span class="view">view</span><span>cart</span></div></div>
        <div class="product" style="left:108px;top:0"><div class="title side" style="top:34px">Hollie</div><div class="photo bag-white" style="left:48px;top:12px;width:48px;height:80px" role="img" aria-label="Adult dog food bag"></div><div class="btns" style="left:15px;top:102px"><span class="price">$43.95</span><span class="view">view</span><span>cart</span></div></div>
      </div>
      <div class="cell" style="left:222px;top:231px;width:227px;height:124px;border-bottom:none">
        <div class="product" style="left:0;top:0"><div class="title side" style="top:32px;left:6px">Hollie</div><div class="photo bag-green" style="left:44px;top:12px;width:48px;height:80px" role="img" aria-label="Lite dog food bag"></div><div class="btns" style="left:12px;top:102px"><span class="price">$43.95</span><span class="view">view</span><span>cart</span></div></div>
        <div class="product" style="left:112px;top:0"><div class="title side" style="top:32px;left:10px">Hollie</div><div class="photo bag-white" style="left:45px;top:12px;width:48px;height:80px" role="img" aria-label="Adult dog food bag"></div><div class="btns" style="left:16px;top:102px"><span class="price">$43.95</span><span class="view">view</span><span>cart</span></div></div>
      </div>
    </section>
  </main>

  <footer class="abs footer"><span>FURNEST MARKET</span></footer>
</div>
</body>
</html>
```